Wine Label Design

Organization name: Orvell Wine Company

My company is called Orvell Wine Company, I’m a wine importer and wholesaler who distributes wine domestically.

We are about to launch a line of three premium and one sparkling wine that we will wholesale to various retailers, wine stores, and restaurants for re-sale. The wines label will have “Dean Marlowe” I plan on having the labels the same and just changing the varietal as needed. My wine are made from premium grapes and will be marketed as a high end wine. My current label size is 3 1/2" wide by 5" in long and the labels can be on a solid background or transparent.

I would like the first label to be for my Cabernet Sauvignon, California, 2012, 750ML (for the size of the bottle) and ALC 13.8% BY VOL (for the alcohol content).

Colors: I am open to any and all designs that would alter my perception of what will be best!

Further:
Current label is boring and poorly done, so hopefully you designers can come up with something better

Industry/Entity Type

It Company

```html
<!DOCTYPE html>
<html lang="en">
<head>
<meta charset="UTF-8">
<title>Dean Marlowe — Cabernet Sauvignon Label</title>
<link rel="stylesheet" href="https://fonts.googleapis.com/css2?family=Pathway+Gothic+One&family=Montserrat:wght@400&display=swap">
<style>
  :root {
    --page: #ffffff;
    --label: #000000;
    --gold: #b98c48;
    --green: #0a8341;
  }
  html, body {
    margin: 0;
    padding: 0;
    width: 1200px;
    height: 924px;
    overflow: hidden;
    background: var(--page);
  }
  .canvas {
    position: relative;
    width: 1200px;
    height: 924px;
  }
  .label {
    position: absolute;
    left: 423px;
    top: 190px;
    width: 353px;
    height: 543px;
    background: var(--label);
  }
  .ornament {
    position: absolute;
    display: block;
  }
  .ornament-top {
    left: 73px;
    top: 44px;
    width: 208px;
    height: 160px;
  }
  .ornament-bottom {
    left: 44px;
    top: 312px;
    width: 266px;
    height: 186px;
  }
  .wine-name {
    position: absolute;
    left: 0;
    right: 0;
    top: 223px;
    margin: 0;
    text-align: center;
    font-family: "Pathway Gothic One", "Arial Narrow", sans-serif;
    font-weight: 400;
    font-size: 47px;
    line-height: 1;
    letter-spacing: 1.5px;
    color: var(--green);
  }
  .varietal {
    position: absolute;
    left: 0;
    right: 0;
    top: 275px;
    margin: 0;
    text-align: center;
    font-family: "Montserrat", Arial, sans-serif;
    font-size: 11px;
    letter-spacing: 0.5px;
    color: var(--gold);
  }
  .spec {
    position: absolute;
    margin: 0;
    font-family: "Montserrat", Arial, sans-serif;
    color: var(--gold);
    line-height: 1;
  }
  .spec-volume {
    left: 118px;
    top: 479px;
    font-size: 11px;
  }
  .spec-alcohol {
    left: 195px;
    top: 481px;
    font-size: 9.5px;
  }
</style>
</head>
<body>
  <main class="canvas">
    <section class="label">
      <svg class="ornament ornament-top" viewBox="0 0 208 160" role="img" aria-label="Symmetrical geometric ornament of gold and green triangles and hexagons">
        <defs>
          <radialGradient id="top-tone" cx="0.5" cy="0.5" r="0.5">
            <stop offset="0" stop-color="#b98c48" stop-opacity="0.85"/>
            <stop offset="0.55" stop-color="#0a8341" stop-opacity="0.45"/>
            <stop offset="1" stop-color="#000000" stop-opacity="0"/>
          </radialGradient>
        </defs>
        <rect width="208" height="160" fill="url(#top-tone)"/>
      </svg>

      <h1 class="wine-name">DEAN MARLOWE</h1>
      <p class="varietal">Cabernet sauvignon, California, 2012</p>

      <svg class="ornament ornament-bottom" viewBox="0 0 266 186" role="img" aria-label="Symmetrical geometric ornament of gold and green triangles with a central hexagon column">
        <defs>
          <radialGradient id="bottom-tone" cx="0.5" cy="0.42" r="0.5">
            <stop offset="0" stop-color="#b98c48" stop-opacity="0.85"/>
            <stop offset="0.55" stop-color="#0a8341" stop-opacity="0.45"/>
            <stop offset="1" stop-color="#000000" stop-opacity="0"/>
          </radialGradient>
        </defs>
        <rect width="266" height="186" fill="url(#bottom-tone)"/>
      </svg>

      <p class="spec spec-volume">750ML</p>
      <p class="spec spec-alcohol">ALC 13.8%</p>
    </section>
  </main>
</body>
</html>
```